Business Card Design

Cake decorating business in a small town in Australia. looking for a style that is fresh with a touch of vintage/country. liking these ideas, timber backgrounds, chalkboards, bunting, flowers and cake elements (rolling pins, cupcakes, cake stands, etc.) would consider a shot saying/statement. would like the back of the card to have wording "Specialising in delectable treats for all your special occasions" - wedding cakes - birthday cakes - special occasion cakes - novelty cakes - cupcakes, cookies, slices and cake pops. maybe incorporate a cake in design on back page. attached are a few of my favourite cakes and the start of a card design I liked.

Industry/Entity Type

Business

Contact Information for Business Card

Marigold's Sugared Bakes 0438 056 969Find me on (Chatterbox Logo)

Requirements
Nice to have
• timber, some of my designs, chalkboard, baking utensils
Should not have
• no red font

```html
<!DOCTYPE html>
<html lang="en">
<head>
<meta charset="utf-8">
<title>Marigold's Sugared Bakes – Business Card</title>
<link href="https://fonts.googleapis.com/css2?family=Delius&family=Nunito:wght@400;600&display=swap" rel="stylesheet">
<style>
  :root {
    --bg: #e9eaec;
    --cocoa: #3a2e2c;
    --pink: #e7a3cf;
    --pink-light: #f2c3e2;
    --cream: #ffffff;
    --band-edge: #f0cde3;
    --ink: #2b2221;
    --contact: #f1eeee;
    --icon: #e8b3cf;
    --cake-warm: #c88a5a;
    --cake-pink: #f5b5cf;
  }
  * { box-sizing: border-box; margin: 0; padding: 0; }
  html, body { width: 1200px; height: 900px; overflow: hidden; }
  body {
    background: var(--bg);
    font-family: "Nunito", sans-serif;
    position: relative;
  }
  .card {
    position: absolute;
    left: 250px;
    width: 700px;
    height: 400px;
    background: var(--cocoa);
    overflow: hidden;
    box-shadow: 0 10px 24px rgba(0,0,0,0.18);
  }
  .card--front { top: 33px; }
  .card--back { top: 467px; }

  .pink-field {
    position: absolute;
    background: linear-gradient(160deg, var(--pink-light) 0%, var(--pink) 100%);
  }
  .card--front .pink-field { left: 0; top: 0; width: 100%; height: 150px; }

  .name-band {
    position: absolute;
    left: 0; top: 100px;
    width: 100%; height: 96px;
    background: var(--cream);
    border-top: 3px solid var(--band-edge);
    border-bottom: 3px solid var(--band-edge);
    display: flex;
    align-items: center;
    justify-content: center;
  }
  .business-name {
    font-family: "Delius", cursive;
    font-weight: 400;
    font-size: 44px;
    color: var(--ink);
    letter-spacing: 0.5px;
    white-space: nowrap;
  }

  .contact {
    position: absolute;
    left: 150px; top: 258px;
    list-style: none;
    color: var(--contact);
    font-size: 25px;
    letter-spacing: 1px;
  }
  .contact li { display: flex; align-items: center; gap: 12px; margin-bottom: 14px; }
  .contact li:nth-child(2) { margin-left: -18px; }
  .contact-icon { width: 26px; height: 26px; flex: none; }
  .social-dot {
    width: 22px; height: 22px; flex: none;
    border-radius: 4px; background: var(--icon);
  }

  /* back */
  .card--back .pink-field { right: 0; top: 0; width: 56%; height: 100%; }
  .cake-art {
    position: absolute;
    right: 40px; top: 30px;
    width: 330px; height: 340px;
    border-radius: 40px;
    background: radial-gradient(ellipse at 45% 50%, var(--cake-pink) 0%, var(--cake-warm) 70%, rgba(200,138,90,0) 100%);
  }
  .tagline {
    position: absolute;
    left: 40px; top: 40px;
    width: 250px;
    font-size: 11px;
    line-height: 1.7;
    letter-spacing: 1px;
    text-transform: uppercase;
    color: var(--pink-light);
    white-space: nowrap;
  }
</style>
</head>
<body>

<section class="card card--front">
  <div class="pink-field"></div>
  <div class="name-band">
    <h1 class="business-name">Marigold's Sugared Bakes</h1>
  </div>
  <ul class="contact">
    <li>
      <svg class="contact-icon" viewBox="0 0 26 26" aria-hidden="true">
        <circle cx="13" cy="13" r="13" fill="var(--icon)"/>
        <path d="M6 11 Q13 5 20 11 L18 13 L16 11 L10 11 L8 13 Z M8 14 H18 V19 H8 Z" fill="var(--cocoa)"/>
      </svg>
      <span>0472 613 284</span>
    </li>
    <li>
      <span class="social-dot" aria-hidden="true"></span>
      <span>/marigoldssugaredbakes</span>
    </li>
  </ul>
</section>

<section class="card card--back">
  <div class="pink-field" role="img" aria-label="Pink striped backdrop behind the cake illustration"></div>
  <div class="cake-art" role="img" aria-label="Illustration of tiered cakes on a cake stand and a birthday cake with candles"></div>
  <p class="tagline">Specialising in delectable treats<br>for all your special occasions</p>
</section>

</body>
</html>
```